Feldwende Bureau GmbH needs a Letterhead

Need a Letter/Card head based on the logo and Webpage design.
To be used for Business letters and One-Page Handouts with the discription of our different Services.
Cards to be used as Flyers to print on different Topics.
Should be Topic nutral as we do Sabbatical-Consultancy, Coaching, Job-Coaching and Vision-Board Workshops (more to come). See www.feldwendebureau.ch

Target Market(s)

Individuales who need Sabbatical-Support/Coaching/JOB-Coaching
Companies who want to give me a mandate as Business Coach

Industry/Entity Type

Business

Font styles to use
Other font styles liked:
• Verdana

Colors
9ccb3b
3277b5
aaaaaa
eaeaea

Requirements
Must have
• Background White or light gray
• not to big/present the Information on Company-Adresse/phone/email/web/offices
• Use the Logo (chair) in a creative way
• Please use following Colors:
• Green: R141, G198, B63
• Blue: R28, G117, B188
• Darkgray: R109, G110, B113
• Lightgray: R209, G211, B212
Should not have
• Wrong Colors!
• Use mentioned Color codes above.

```html
<!DOCTYPE html>
<html lang="en">
<head>
<meta charset="utf-8">
<title>Feldwende Bureau GmbH – Letterhead</title>
<link rel="stylesheet" href="https://fonts.googleapis.com/css2?family=Carlito&family=Montserrat:wght@400;500&display=swap">
<style>
  :root{
    --green:#8dc63f;
    --blue:#1c75bc;
    --darkgray:#6d6e71;
    --lightgray:#d1d3d4;
    --backdrop:#eaeaea;
    --ink:#1e1e1e;
    --paper:#ffffff;
  }
  html,body{margin:0;padding:0;width:1200px;height:1200px;overflow:hidden;background:var(--backdrop);}
  .letterhead{
    position:absolute;left:175px;top:0;width:849px;height:1200px;
    background:var(--paper);overflow:hidden;
    font-family:"Carlito",sans-serif;color:var(--ink);
  }
  .brand{
    position:absolute;top:70px;left:0;width:100%;
    display:flex;justify-content:center;align-items:center;gap:14px;
  }
  .brand-dot{width:26px;height:26px;border-radius:50%;background:var(--green);}
  .brand-name{font-family:"Carlito",sans-serif;font-size:40px;color:var(--darkgray);letter-spacing:1px;}
  .body-text{
    position:absolute;left:92px;margin:0;
    font-size:15px;line-height:29.8px;white-space:nowrap;
  }
  .greeting{top:207px;}
  .para-1{top:266px;}
  .para-2{top:476px;}
  .para-3{top:625px;}
  .closing{top:866px;}
  .signer{top:985px;}
  .signature{
    position:absolute;left:90px;top:906px;width:212px;height:74px;
    background:linear-gradient(90deg,#f3f3f3,#e6e6e6);border-radius:4px;
  }
  .footer-address{
    position:absolute;top:1112px;left:0;width:850px;text-align:center;
    font-family:"Montserrat",sans-serif;font-size:9.6px;line-height:14px;color:var(--ink);
    white-space:nowrap;
  }
  .footer-address .label{color:var(--blue);}
  .footer-band{position:absolute;left:0;top:1150px;width:849px;height:50px;}
  .footer-contact{
    position:absolute;top:1158px;left:0;width:850px;text-align:center;
    font-family:"Montserrat",sans-serif;font-size:10px;color:#fff;word-spacing:1px;
    white-space:nowrap;
  }
</style>
</head>
<body>
<main class="letterhead">
  <header class="brand">
    <span class="brand-dot"></span>
    <span class="brand-name">Feldwende Bureau</span>
  </header>

  <p class="body-text greeting">Lorem Ipsum is simply</p>

  <p class="body-text para-1">&nbsp;dummy text of the printing and typesetting industry. Lorem Ipsum has been the industry's<br>standard dummy text ever since the 1500s, when an unknown printer took a galley of type and<br>scrambled it to make a type specimen book. It has survived not only five centuries, but also the<br>leap into electronic typesetting, remaining essentially unchanged. It was popularised in the 1960s<br>with the release of Typeleaf sheets containing Lorem Ipsum passages, and more recently with<br>desktop publishing software like Pressline Composer including versions of Lorem Ipsum.</p>

  <p class="body-text para-2">It is a long established fact that a reader will be distracted by the readable content of a page<br>when looking at its layout. The point of using Lorem Ipsum is that it has a more-or-less normal<br>distribution of letters, as opposed to using 'Content here, content here', making it look like<br>readable English. Many desktop publishing packages and web page editors now use.</p>

  <p class="body-text para-3">&nbsp;Contrary to popular belief, Lorem Ipsum is not simply random text. It has roots in a piece of<br>classical Latin literature from 45 BC, making it over 2000 years old. Robert Hallworth, a Latin<br>professor at Ashford Hill College in Vermont, looked up one of the more obscure Latin<br>words, consectetur, from a Lorem Ipsum passage, and going through the cites of the word in<br>classical literature, discovered the undoubtable source. Lorem Ipsum comes from sections<br>1.10.32 and 1.10.33 of "de Finibus Bonorum et Malorum" (The Extremes of Good and Evil) by<br>Lucius Aemilian, written in 45 BC. This book</p>

  <p class="body-text closing">Lorem Ipsum</p>
  <div class="signature" role="img" aria-label="Handwritten signature"></div>
  <p class="body-text signer">Lorem Ipsum is a dummy</p>

  <div class="footer-address">
    <span class="label">Firmenanschrift:</span> Feldwende Bureau GmbH, Lena Ammann, Sonnhaldenweg 14, 4999 Mosbrugg, Schweiz<br>
    <span class="label">Büros:</span> Mosbrugg, Talgau, am Brunnenplatz, Hallwiesen
  </div>

  <svg class="footer-band" viewBox="0 0 849 50" aria-hidden="true">
    <path d="M0 0 H700 Q712 20 726 31 H0 Z" fill="var(--blue)"/>
  </svg>
  <div class="footer-contact">P: +41 (0) 79 000 12 34 &nbsp; E: lena.ammann@feldwendebureau.ch &nbsp; W: www.feldwendebureau.ch</div>
</main>
</body>
</html>
```